qTorvanix - A forward thinking technology company in the greater Silicon Valley

A .ppt slide deck for a software consulting company. This slide deck will be used for project kick off meetings, sales proposals, and presentations to large audiences that report progress on a variety of projects. It should catch the eye with appealing creativity. Allow for flexibility in space and display. Project well both virtually and in person under varying light conditions. The finished product should give the impression that we are a custom shop but balance in appeal to larger, more traditional companies.

Review of the designs has been delayed due to holiday travel. Thank you for your submissions. I look forward to getting back to you the week of December 3rd.

Target Market(s)

We are an innovative technology company in the greater Silicon Valley. We design and build custom business analytics tools for large, retail corporations. Our solutions deal primarily in the supply chain space but we are leaning towards commercial construction and telecommunications industries. We are targeting prospective clients interested in machine learning and artificial intelligence. Our customers know quality and will pay for a custom solution that exceeds their expectations.

Industry/Entity Type

Business Software

Font styles to use
Sans Serif

Colors

Designer to choose colors to be used in the design.

Requirements
Must have
• Color, graphics, and photos. Multiple different template pages to appeal for graphs, pictures, text, or timelines.
Should not have
• Anything that resembles a "fidget spinner."

```html
<!DOCTYPE html>
<html lang="en">
<head>
<meta charset="utf-8">
<title>qTorvanix – Our Awesome People</title>
<link rel="stylesheet" href="https://fonts.googleapis.com/css2?family=Montserrat:wght@500;800&family=Roboto:wght@400;700&display=swap">
<style>
  :root {
    --slide-bg: #1f1f1f;
    --corner-black: #000000;
    --numeral-fill: #262626;
    --numeral-stroke: #bdbdbd;
    --accent-green: #9bc25a;
    --accent-olive: #6b7040;
    --text-white: #ffffff;
    --text-muted: #8a8a8a;
    --placeholder: #8f8f8f;
    --frame: #555555;
  }
  html, body {
    margin: 0;
    padding: 0;
    overflow: hidden;
    background: var(--slide-bg);
  }
  .slide {
    position: relative;
    width: 1200px;
    height: 678px;
    overflow: hidden;
    background: var(--slide-bg);
    font-family: "Montserrat", sans-serif;
  }
  .slide-graphics {
    position: absolute;
    inset: 0;
  }
  .brand {
    position: absolute;
    left: 33px;
    top: 30px;
    display: flex;
    align-items: center;
    gap: 8px;
    font-family: "Montserrat", sans-serif;
    font-weight: 500;
    font-size: 13px;
    letter-spacing: 1px;
    color: var(--text-muted);
  }
  .brand-mark {
    width: 10px;
    height: 10px;
    background: var(--accent-green);
  }
  .site-url {
    position: absolute;
    left: 970px;
    top: 31px;
    font-family: "Roboto", sans-serif;
    font-size: 11px;
    color: var(--text-muted);
  }
  .page-number {
    position: absolute;
    left: 1158px;
    top: 31px;
    font-family: "Roboto", sans-serif;
    font-size: 11px;
    color: var(--text-muted);
  }
  .image-drop {
    position: absolute;
    left: 578px;
    top: 296px;
    width: 42px;
    height: 62px;
    border-radius: 4px;
    background: var(--placeholder);
    opacity: 0.75;
  }
  .image-drop-label {
    position: absolute;
    left: 540px;
    top: 314px;
    margin: 0;
    font-family: "Roboto", sans-serif;
    font-weight: 700;
    font-size: 12px;
    line-height: 17px;
    color: var(--text-white);
  }
  .section-title {
    position: absolute;
    left: 134px;
    top: 364px;
    margin: 0;
    font-family: "Montserrat", sans-serif;
    font-weight: 800;
    font-size: 67px;
    line-height: 82px;
    color: var(--text-white);
  }
  .service-list {
    position: absolute;
    left: 664px;
    top: 564px;
    margin: 0;
    padding: 0;
    list-style: none;
    display: flex;
    gap: 22px;
    font-family: "Roboto", sans-serif;
    font-weight: 700;
    font-size: 17px;
    color: var(--text-white);
  }
</style>
</head>
<body>
<main class="slide">
  <svg class="slide-graphics" width="1200" height="678" viewBox="0 0 1200 678" aria-hidden="true">
    <polygon class="corner-wedge" points="0,0 290,0 0,290" fill="var(--corner-black)"/>
    <line x1="290" y1="0" x2="0" y2="290" stroke="var(--numeral-stroke)" stroke-width="1"/>
    <line class="accent-rule" x1="593" y1="0" x2="257" y2="334" stroke="var(--accent-olive)" stroke-width="1"/>
    <line class="accent-rule" x1="1066" y1="435" x2="943" y2="558" stroke="var(--accent-olive)" stroke-width="1"/>

    <g class="section-numeral" fill="var(--numeral-fill)" stroke="var(--numeral-stroke)" stroke-width="1.2">
      <path class="numeral-zero" fill-rule="evenodd"
            d="M525,143 C602,143 665,220 665,316 C665,413 602,490 525,490 C448,490 385,413 385,316 C385,220 448,143 525,143 Z
               M526,210 C489,210 459,259 459,320 C459,380 489,429 526,429 C563,429 593,380 593,320 C593,259 563,210 526,210 Z"/>
      <path class="numeral-one" d="M678,151 H813 V482 H738 V214 H678 Z"/>
    </g>

    <polygon class="corner-accent" points="1200,566 1200,678 1094,678" fill="var(--accent-green)"/>
    <rect x="0.5" y="0.5" width="1199" height="677" fill="none" stroke="var(--frame)" stroke-width="1"/>
  </svg>

  <div class="brand"><span class="brand-mark"></span>qTorvanix</div>
  <div class="site-url">www.qtorvanixlabs.com</div>
  <div class="page-number">2</div>

  <div class="image-drop" role="img" aria-label="Image placeholder for a team photo"></div>
  <p class="image-drop-label">Drop your image here<br>Drop your image here</p>

  <h1 class="section-title">OUR<br>AWESOME<br>PEOPLE.</h1>

  <ul class="service-list">
    <li>Design.</li>
    <li>Promotion.</li>
    <li>Media.</li>
    <li>Photography.</li>
  </ul>
</main>
</body>
</html>
```